Business card design for Plumbing and Gas fitting company

We need a business card design for our plumbing and gas fitting company using the company logo and director details. Design should be modern and eye-catching however kept reasonably simple. This design should be targeted at commercial businesses/work so professionalism is key.

Target Market(s)

Commercial/business

Industry/Entity Type

Plumbing

Contact Information for Business Card

Warren Dohey
Director
027 581 9043
warren@vantorplumbingandgas.example
PO Box 7816
Palmerston North 4472

Font styles to use
Sans Serif

Requirements
Must have
• Logo
• Modern
• Kept simple
Nice to have
• Colour scheme based around logo

```html
<!DOCTYPE html>
<html lang="en">
<head>
<meta charset="utf-8">
<title>Vantor Plumbing &amp; Gas – Business Card</title>
<link rel="stylesheet" href="https://fonts.googleapis.com/css2?family=Open+Sans:wght@400;600;700&display=swap">
<style>
  :root {
    --backdrop: #e9e6e2;
    --card: #262626;
    --card-edge: #1c1c1c;
    --brand-blue: #1f7ac4;
    --brand-orange: #ee7a2a;
    --text-light: #c9c9c9;
    --text-muted: #a8a8a8;
    --mark-grey: #8a8a8a;
  }
  * { box-sizing: border-box; margin: 0; padding: 0; }
  html, body {
    width: 1200px; height: 1000px; overflow: hidden;
    background: var(--backdrop);
    font-family: "Open Sans", Arial, sans-serif;
  }
  .canvas { position: relative; width: 1200px; height: 1000px; }
  .card {
    position: absolute; left: 267px; width: 665px; height: 396px;
    background: var(--card);
    border-radius: 24px; overflow: hidden;
    box-shadow: 0 6px 14px rgba(0,0,0,.35);
  }
  .card--front { top: 75px; }
  .card--back { top: 535px; }

  .brand-name {
    position: absolute; left: 31px; top: 118px;
    font-size: 26px; font-weight: 700; letter-spacing: -0.3px;
    color: var(--brand-blue);
  }
  .person { position: absolute; left: 32px; top: 220px; }
  .person__name {
    font-size: 18px; font-weight: 700; letter-spacing: .5px;
    color: var(--brand-blue); text-transform: uppercase;
  }
  .person__role { font-size: 16px; color: var(--text-muted); margin-top: 1px; }

  .contact { position: absolute; left: 32px; top: 284px; list-style: none; }
  .contact__item {
    display: flex; align-items: center; gap: 7px;
    font-size: 16px; color: var(--text-light); line-height: 25px;
  }
  .contact__item--address { margin-top: 4px; }
  .contact__icon { width: 12px; height: 14px; flex: none; }

  .accent-stripe { position: absolute; left: 0; bottom: 0; width: 100%; height: 10px; }

  .back-brand {
    position: absolute; left: 0; right: 0; top: 168px;
    text-align: center;
    font-size: 40px; font-weight: 700; letter-spacing: -0.5px;
    color: var(--mark-grey);
  }
</style>
</head>
<body>
<main class="canvas">

  <section class="card card--front" aria-label="Business card front">
    <div class="brand-name">Vantor Plumbing &amp; Gas</div>

    <div class="person">
      <div class="person__name">Warren Dohey</div>
      <div class="person__role">Managing Director</div>
    </div>

    <ul class="contact">
      <li class="contact__item">
        <svg class="contact__icon" viewBox="0 0 12 14" aria-hidden="true">
          <rect x="2.5" y="0.8" width="7" height="12.4" rx="1.3" fill="none" stroke="var(--brand-blue)" stroke-width="1.4"/>
          <circle cx="6" cy="11" r="0.8" fill="var(--brand-blue)"/>
        </svg>
        027 581 9043
      </li>
      <li class="contact__item">
        <svg class="contact__icon" viewBox="0 0 12 14" aria-hidden="true">
          <rect x="0" y="3" width="12" height="8.5" fill="var(--brand-blue)"/>
          <path d="M0.5 3.5 L6 8 L11.5 3.5" fill="none" stroke="var(--card)" stroke-width="1.1"/>
        </svg>
        warren@vantorplumbingandgas.example
      </li>
      <li class="contact__item contact__item--address">PO Box 7816 Palmerston North 4472</li>
    </ul>

    <svg class="accent-stripe" viewBox="0 0 665 10" preserveAspectRatio="none" aria-hidden="true">
      <polygon points="0,0 530,0 540,10 0,10" fill="var(--brand-blue)"/>
      <polygon points="530,0 536,0 546,10 540,10" fill="var(--card-edge)"/>
      <polygon points="536,0 665,0 665,10 546,10" fill="var(--brand-orange)"/>
    </svg>
  </section>

  <section class="card card--back" aria-label="Business card back">
    <div class="back-brand">Vantor Plumbing &amp; Gas</div>
  </section>

</main>
</body>
</html>
```